Business Card Design Project - Small Bar

We would like a design for a business card for our new small bar in Melbourne. It is quite the 'hipster' bar and the card would need to reflect this in its design. We do have a logo which needs to be used in the card, tho how it is incorporated is up to you! :)

OK, the Bar currently has a common 'inner city' vibe, i.e. random artwork, older 30s/40's club furniture, grafitti murals on the walls, eclectic objects etc etc Current clientele would be described as "hipster", "urban professional" etc. How to describe... they are 30, have a good job but have beards, beanies and own vinyl records. :)

The card will be used to give to professional contacts and to bands/solo artists we come across to invite them to come play at our venue, so somehow I would like it to convey the image of 'professional' and 'funky' all in one. Difficult I know.

I have asked for some advice on making this brief clearer, so check back.

Thanks all in advance. :)
Updates

Sorry all

I've now been told that it is HARBOUR WEST 3009. Apparently we are on the border and it is referred to by either west or north Melbourne, but it is definitely HARBOUR WEST 3009.

Things you learn hey? :)

Target Market(s)

Hipsters, urbanites, the inner city crowd

Industry/Entity Type

Artists

Requirements
Must have
• Logo (JPG file attached)
Name of the bar "The Lantern & Otter"
Address - 742 Brindle St, North Melbourne, Victoria 3051
Names - Owen Partridge, Lewis Dunhurst
mobile. 0417265093 and 0456302714
Obviously we would need separate cards?
Nice to have
• Facebook link
Facebook 'like' icon
Should not have
• traditional designs. I am looking for something unique and funky. with FUNK! :)

```html
<!DOCTYPE html>
<html lang="en">
<head>
<meta charset="utf-8">
<title>The Lantern &amp; Otter — Business Card</title>
<link rel="stylesheet" href="https://fonts.googleapis.com/css2?family=Bebas+Neue&family=Questrial&display=swap">
<style>
  :root {
    --page: #e8e8e8;
    --card-dark: #2b2b2c;
    --mint: #9fd3b4;
    --green: #3e9a6a;
    --ink: #1e1e1f;
    --text-light: #e6e6e6;
    --shadow: rgba(0, 0, 0, 0.35);
  }
  * { box-sizing: border-box; margin: 0; padding: 0; }
  html, body { width: 912px; height: 1200px; overflow: hidden; }
  body {
    background: var(--page);
    font-family: "Questrial", Arial, sans-serif;
    position: relative;
  }
  .card {
    position: absolute;
    left: 106px;
    width: 700px;
    height: 400px;
    background: var(--card-dark);
    box-shadow: 0 14px 28px var(--shadow);
    overflow: hidden;
  }
  .card--front { top: 170px; }
  .card--back { top: 630px; }

  .front__band {
    position: absolute;
    left: 0; top: 0;
    width: 700px;
    height: 164px;
    display: block;
  }
  .brand {
    position: absolute;
    display: flex;
    align-items: center;
    gap: 14px;
  }
  .brand__mark {
    width: 46px; height: 46px;
    border-radius: 50%;
    flex: none;
  }
  .brand__name {
    font-family: "Bebas Neue", Impact, sans-serif;
    letter-spacing: 0.5px;
    line-height: 1;
    white-space: nowrap;
  }
  .card--front .brand { left: 42px; top: 52px; }
  .card--front .brand__mark { background: var(--ink); }
  .card--front .brand__name { font-size: 42px; color: var(--ink); }

  .contact {
    position: absolute;
    left: 52px;
    top: 196px;
    color: var(--text-light);
    font-size: 15px;
    line-height: 1.25;
  }
  .contact__address { margin-bottom: 26px; }
  .contact__list { list-style: none; }
  .contact__item {
    display: flex;
    align-items: center;
    gap: 9px;
    height: 26px;
    white-space: nowrap;
  }
  .contact__icon { width: 12px; height: 12px; flex: none; }
  .like-badge {
    width: 54px; height: 18px;
    background: #f2f2f2;
    border: 1px solid #c9c9c9;
    border-radius: 3px;
    margin-left: 8px;
  }
  .person-name {
    position: absolute;
    right: 70px;
    top: 226px;
    color: var(--mint);
    font-size: 22px;
    white-space: nowrap;
  }

  .card--back .brand {
    left: 0; right: 0; top: 150px;
    justify-content: center;
  }
  .card--back .brand__mark { width: 60px; height: 60px; background: var(--mint); }
  .card--back .brand__name { font-size: 60px; color: var(--mint); }
  .back__web {
    position: absolute;
    right: 118px;
    top: 222px;
    color: var(--mint);
    font-size: 16px;
    white-space: nowrap;
  }
</style>
</head>
<body>
  <section class="card card--front" aria-label="Business card front">
    <svg class="front__band" viewBox="0 0 700 164" aria-hidden="true">
      <defs>
        <pattern id="band-teeth" x="0" y="148" width="20" height="14" patternUnits="userSpaceOnUse">
          <polygon points="0,0 20,0 10,14" fill="#9fd3b4"/>
        </pattern>
      </defs>
      <rect x="0" y="0" width="700" height="148.5" fill="#9fd3b4"/>
      <rect x="0" y="148" width="700" height="14" fill="url(#band-teeth)"/>
    </svg>

    <div class="brand">
      <span class="brand__mark"></span>
      <span class="brand__name">The Lantern &amp; Otter</span>
    </div>

    <div class="contact">
      <p class="contact__address">742 Brindle St,<br>HARBOUR WEST 3009</p>
      <ul class="contact__list">
        <li class="contact__item">
          <svg class="contact__icon" viewBox="0 0 12 12" aria-hidden="true"><rect x="3" y="0.5" width="6" height="11" rx="1" fill="none" stroke="#e6e6e6"/><circle cx="6" cy="9.5" r="0.8" fill="#e6e6e6"/></svg>
          0456302714
        </li>
        <li class="contact__item">
          <svg class="contact__icon" viewBox="0 0 12 12" aria-hidden="true"><rect x="0.5" y="2.5" width="11" height="7" fill="none" stroke="#e6e6e6"/><polyline points="0.5,2.5 6,7 11.5,2.5" fill="none" stroke="#e6e6e6"/></svg>
          info@lanternotter.com
        </li>
        <li class="contact__item">
          <svg class="contact__icon" viewBox="0 0 12 12" aria-hidden="true"><circle cx="6" cy="6" r="5.3" fill="none" stroke="#e6e6e6"/><ellipse cx="6" cy="6" rx="2.3" ry="5.3" fill="none" stroke="#e6e6e6"/><line x1="0.7" y1="6" x2="11.3" y2="6" stroke="#e6e6e6"/></svg>
          www.lanternotter.com
        </li>
        <li class="contact__item">
          <svg class="contact__icon" viewBox="0 0 12 12" aria-hidden="true"><rect x="0" y="0" width="12" height="12" rx="1.5" fill="#e6e6e6"/></svg>
          lanternotter.social/bar
          <span class="like-badge"></span>
        </li>
      </ul>
    </div>

    <p class="person-name">Lewis Dunhurst</p>
  </section>

  <section class="card card--back" aria-label="Business card back">
    <div class="brand">
      <span class="brand__mark"></span>
      <span class="brand__name">The Lantern &amp; Otter</span>
    </div>
    <p class="back__web">www.lanternotter.com</p>
  </section>
</body>
</html>
```